" Ao formar uma turma eu leciono os cursos da área de engenharia civil e um local que alugo. Elaboro também projetos de edificações quando solicitado. Desenvolvo planilhas e quenos softwares na área de engenharia de estruturas que acelere o processo de confecção de tarefas no calculo estrutural de uma edificação. "

```html
<!DOCTYPE html>
<html lang="pt-BR">
<head>
<meta charset="utf-8">
<title>Vantori – Papel timbrado</title>
<link rel="stylesheet" href="https://fonts.googleapis.com/css2?family=Montserrat:wght@400;600;700&display=swap">
<style>
  :root {
    --backdrop: #e9eaec;
    --paper: #ffffff;
    --navy: #2b2f6b;
    --cyan: #29a8e0;
    --ink: #3a3d55;
    --muted: #7a7d8c;
    --ghost: #ececee;
  }
  * { margin: 0; padding: 0; box-sizing: border-box; }
  html, body {
    width: 1200px; height: 1200px; overflow: hidden;
    background: var(--backdrop);
    font-family: "Montserrat", sans-serif;
  }
  .letterhead {
    position: absolute;
    left: 197px; top: 30px;
    width: 806px; height: 1140px;
    background: var(--paper);
    box-shadow: 0 6px 24px rgba(0,0,0,0.12);
    overflow: hidden;
  }
  .brand {
    position: absolute;
    right: 70px; top: 70px;
    text-align: center;
  }
  .brand-row {
    display: flex; align-items: center; justify-content: center; gap: 14px;
  }
  .brand-square {
    width: 34px; height: 34px; background: var(--cyan);
  }
  .brand-name {
    font-weight: 700; font-size: 52px; color: var(--navy);
    letter-spacing: 1px; line-height: 1;
  }
  .brand-tagline {
    margin-top: 10px;
    font-size: 11.5px; font-weight: 600; letter-spacing: 3px;
    color: var(--navy);
  }
  .ghost-mark {
    position: absolute;
    left: 283px; top: 400px;
    width: 240px; height: 240px;
    background: var(--ghost);
  }
  .rule {
    position: absolute; left: 60px; right: 60px; height: 3px;
    background: var(--cyan);
  }
  .rule-top { top: 900px; }
  .rule-bottom { top: 1068px; left: 380px; }
  .contact {
    position: absolute; left: 70px; top: 925px;
    font-size: 14px; line-height: 1.75; color: var(--ink);
  }
  .contact .label { color: var(--muted); margin-right: 6px; }
  .website {
    position: absolute; right: 70px; top: 1036px;
    font-size: 14px; color: var(--ink);
  }
  .website .label { color: var(--muted); margin-right: 6px; }
  .footer-band {
    position: absolute; left: 0; right: 0; bottom: 0; height: 44px;
    background: var(--navy);
  }
</style>
</head>
<body>
  <main class="letterhead">
    <header class="brand">
      <div class="brand-row">
        <span class="brand-square"></span>
        <span class="brand-name">Vantori</span>
      </div>
      <div class="brand-tagline">CURSOS · PROJETOS · CONSULTORIA</div>
    </header>

    <div class="ghost-mark" aria-hidden="true"></div>

    <div class="rule rule-top"></div>
    <address class="contact" style="font-style: normal;">
      <div><span class="label">Phone</span>(11) 3456-7890</div>
      <div><span class="label">Address</span>Rua das Acácias, 420</div>
      <div>Sala 12 - Campinas - 13010-050</div>
    </address>

    <div class="website"><span class="label">Website</span>www.vantori.com.br</div>
    <div class="rule rule-bottom"></div>

    <div class="footer-band"></div>
  </main>
</body>
</html>
```